Custom Home Builder Needs a Website

Harbor Pine Builders Ltd. requires a clean professional 5 page website - Home, About Us, Gallery (Interior and Exterior), Our Process and Contact Us(with registration form). We are a home builder who also has homes for sale. Also please have a place for video embedding. Editable fields by user. Using the stationery 'feel' that is attached. Need social media links. If you require any additional files, please request.

Target Market(s)

Families and professionals

Industry/Entity Type

Home Builder

Coding

Coded - Design and coding required

Number of Pages Required

5+ page

Font styles to use
Sans Serif
Other font styles liked:
• Lato

Requirements
Must have
• Editable by user
• Register Button
• Place to put home models for sale - preferably on the first page
• 5 page website -
• -Home
• -About Us
• -Gallery (Interior and Exterior)
• -Our Process
• -Contact Us.
Nice to have
• Themed similar to current stationery
• place for video embedding
• Try some darker backgrounds
• Change pictures to B/W if works for design
Should not have
• cartoonish type of content

```html
<!DOCTYPE html>
<html lang="en">
<head>
<meta charset="utf-8">
<title>Harbor Pine Builders Ltd.</title>
<link href="https://fonts.googleapis.com/css2?family=Lato:wght@400;700;900&family=Michroma&display=swap" rel="stylesheet">
<style>
:root{
  --green:#1b7f3f;
  --green-light:#2ea35a;
  --dark:#1c1c1c;
  --darker:#141414;
  --panel:#242424;
  --light:#f4f4f4;
  --white:#ffffff;
  --text:#222222;
  --muted:#6a6a6a;
  --blue:#3a6ea8;
}
*{margin:0;padding:0;box-sizing:border-box}
html,body{width:1200px;height:2862px;overflow:hidden}
body{position:relative;background:var(--light);font-family:"Lato",sans-serif;color:var(--text)}
.display{font-family:"Michroma",sans-serif}
.abs{position:absolute}

/* header */
.site-header{position:absolute;left:0;top:0;width:1200px;height:118px;background:var(--dark);border-bottom:4px solid var(--blue);overflow:hidden}
.brand{position:absolute;left:108px;top:14px;display:flex;align-items:center;gap:12px}
.brand-mark{width:22px;height:22px;background:var(--green-light)}
.brand-name{font-family:"Lato",sans-serif;font-weight:900;font-size:27px;color:var(--green-light);letter-spacing:1px;text-transform:uppercase}
.main-nav{position:absolute;left:108px;top:82px;display:flex;gap:37px}
.main-nav a{font-family:"Michroma",sans-serif;font-size:16px;color:var(--white);text-decoration:none;letter-spacing:.5px}
.ribbon{position:absolute;right:-62px;top:30px;width:270px;height:34px;background:var(--green);transform:rotate(45deg);color:var(--white);font-size:14px;font-weight:700;text-align:center;line-height:34px}

/* hero */
.hero{position:absolute;left:0;top:118px;width:1200px;height:573px;background:linear-gradient(180deg,#c8ccd2 0%,#a5a39c 35%,#6f6a62 65%,#4a4540 100%)}
.hero-caption{position:absolute;left:50%;transform:translateX(-50%);top:406px;text-align:center}
.hero-caption span{display:inline-block;background:rgba(20,20,20,.72);color:var(--white);font-family:"Michroma",sans-serif;font-size:31px;letter-spacing:1px;padding:4px 16px;margin-bottom:4px;white-space:nowrap}

/* gallery strip */
.gallery-strip{position:absolute;left:0;top:691px;width:1200px;height:336px;background:var(--light)}
.thumb{position:absolute;top:51px;width:313px;height:225px;background:#e2e2e2;padding:12px;box-shadow:0 0 0 1px #d0d0d0}
.thumb .photo{width:100%;height:100%}
.arrow{position:absolute;top:114px;width:76px;height:88px;background:linear-gradient(180deg,#dcdcdc,#b5b5b5)}
.arrow svg{position:absolute;left:24px;top:28px}

/* mission */
.mission{position:absolute;left:0;top:1027px;width:1200px;height:431px;background:var(--light)}
.mission-photo{position:absolute;left:0;top:0;width:601px;height:364px;background:linear-gradient(180deg,#a9c4e0 0%,#c9d6e0 40%,#a49a84 60%,#7d7260 100%)}
.mission-text{position:absolute;left:637px;top:70px;width:520px}
.section-title{font-family:"Michroma",sans-serif;font-size:22px;color:var(--green);letter-spacing:.5px}
.mission-text .section-title{padding-bottom:8px;border-bottom:2px solid var(--green);display:inline-block;margin-bottom:16px;border-bottom:none}
.mission-text .rule{width:72px;height:2px;background:var(--green);margin:-8px 0 16px}
.mission-text p{font-weight:700;font-size:15.5px;line-height:19px;margin-bottom:17px}
.btn{display:inline-block;background:var(--green);color:var(--white);font-family:"Lato",sans-serif;font-weight:700;text-transform:uppercase;text-align:center}
.mission .btn{width:148px;height:38px;line-height:38px;font-size:15px;margin-top:10px}

/* quote / video */
.quote-band{position:absolute;left:0;top:1458px;width:1200px;height:484px;background:radial-gradient(ellipse at 50% 50%,#2a2a2a 0%,#181818 100%)}
.band-title{position:absolute;font-family:"Michroma",sans-serif;font-size:21px;color:var(--white);letter-spacing:1px}
.band-title::after{content:"";display:block;width:96px;height:2px;background:var(--white);margin-top:10px}
.field{position:absolute;background:var(--white);height:50px;width:231px;font-size:14px;color:#888;padding:0 14px;line-height:50px}
.field.select::after{content:"";position:absolute;right:12px;top:22px;border:5px solid transparent;border-top:6px solid #333}
.field.select{color:#333}
.field.message{height:78px;width:495px;line-height:22px;padding-top:10px}
.submit{position:absolute;left:89px;top:408px;width:150px;height:40px;background:var(--white);color:var(--green);font-weight:700;font-size:15px;text-align:center;line-height:40px;text-transform:uppercase;letter-spacing:1px}
.video{position:absolute;left:640px;top:104px;width:467px;height:283px;background:linear-gradient(180deg,#c9c2b4 0%,#b5a894 50%,#8d8472 100%)}
.video-bar{position:absolute;left:0;bottom:0;width:100%;height:22px;background:rgba(0,0,0,.55)}
.video-progress{position:absolute;left:0;bottom:22px;width:100%;height:3px;background:rgba(255,255,255,.35)}
.video-progress i{display:block;width:18%;height:100%;background:#e22}

/* market */
.market{position:absolute;left:0;top:1942px;width:1200px;height:571px;background:var(--light)}
.market-title{position:absolute;left:0;width:1200px;top:44px;text-align:center;font-family:"Michroma",sans-serif;font-size:22px;color:var(--text);letter-spacing:1px}
.market-title::after{content:"";display:block;width:140px;height:2px;background:var(--text);margin:8px auto 0}
.card{position:absolute;top:113px;width:241px;height:351px;background:var(--white);box-shadow:0 0 0 1px #e1e1e1}
.card .photo{height:160px;background:linear-gradient(180deg,#c3ccd6 0%,#9ea3a4 45%,#6c7a5c 100%)}
.card-body{padding:12px 14px 0}
.card h3{font-size:12.5px;font-weight:700;color:#333;margin-bottom:4px}
.card .meta{font-size:9px;color:#555;line-height:14px}
.card .meta b{font-weight:700}
.card p{font-size:9px;color:#777;line-height:13px;margin-top:6px}
.card .btn{position:absolute;left:0;top:290px;width:109px;height:33px;line-height:33px;font-size:12px}
.load-more{position:absolute;left:527px;top:500px;width:147px;height:39px;line-height:39px;font-size:14px}

/* footer */
.site-footer{position:absolute;left:0;top:2513px;width:1200px;height:292px;background:var(--dark);color:var(--white)}
.footer-col{position:absolute;top:44px}
.footer-col h4{font-family:"Lato",sans-serif;font-weight:900;font-size:17px;text-transform:uppercase;margin-bottom:18px;letter-spacing:.5px}
.footer-col h4 em{font-style:normal;color:var(--green-light)}
.footer-col p,.footer-col li{font-weight:700;font-size:15px;line-height:20px}
.footer-col ul{list-style:none}
.footer-col li{margin-bottom:9px}
.newsletter-input{width:220px;height:37px;background:var(--white);color:#888;font-size:14px;line-height:37px;padding-left:40px;position:relative}
.newsletter-input svg{position:absolute;left:10px;top:11px}
.subscribe{width:220px;height:35px;line-height:35px;font-size:13px;margin-top:10px}
.social{display:flex;gap:26px;margin-top:34px}
.social span{width:13px;height:13px;border-radius:50%;background:var(--white)}
.copyright{position:absolute;left:0;top:2805px;width:1200px;height:57px;background:#2e2e2e;color:var(--white);text-align:center;font-size:15px;line-height:57px;font-weight:700}
.copyright em{font-style:normal;color:var(--green)}
</style>
</head>
<body>

<header class="site-header">
  <div class="brand"><span class="brand-mark"></span><span class="brand-name">Harbor Pine Builders Ltd.</span></div>
  <nav class="main-nav">
    <a>HOME</a><a>ABOUT US</a><a>GALLERY</a><a>OUR PROCESS</a><a>CONTACT US</a>
  </nav>
  <div class="ribbon">How to Get Started</div>
</header>

<section class="hero" role="img" aria-label="Photo of a large craftsman-style two-storey home with stone accents under a grey winter sky">
  <div class="hero-caption">
    <span>FROM YOUR IMAGINATION TO REALITY.</span><br>
    <span>CUSTUM DESIGN HOMES BY THE ALDREN GROUP</span>
  </div>
</section>

<section class="gallery-strip">
  <div class="arrow" style="left:0">
    <svg width="26" height="32" viewBox="0 0 26 32"><path d="M22 2 L4 16 L22 30 Z" fill="#fff"/></svg>
  </div>
  <div class="thumb" style="left:95px"><div class="photo" role="img" aria-label="Interior photo of a bright kitchen with white cabinets and steel appliances" style="background:linear-gradient(160deg,#ece7de,#b9ab94 60%,#5a4a3a)"></div></div>
  <div class="thumb" style="left:443px"><div class="photo" role="img" aria-label="Interior photo of a child's bedroom with pale blue walls" style="background:linear-gradient(160deg,#dfe7ea,#a9bcc4 55%,#8a7f78)"></div></div>
  <div class="thumb" style="left:790px"><div class="photo" role="img" aria-label="Interior photo of a living room with a stone fireplace and cream sofas" style="background:linear-gradient(160deg,#f1efe9,#cfc7b8 55%,#6e6253)"></div></div>
  <div class="arrow" style="right:0">
    <svg width="26" height="32" viewBox="0 0 26 32"><path d="M4 2 L22 16 L4 30 Z" fill="#fff"/></svg>
  </div>
</section>

<section class="mission">
  <div class="mission-photo" role="img" aria-label="Portrait photo of the builder standing in an open prairie field"></div>
  <div class="mission-text">
    <h2 class="section-title">MISSION STATEMENT</h2>
    <div class="rule"></div>
    <p>Lorem ipsum dolor sit amet, consectetur adipisicing elit, sed do eiusmod tempor incididunt ut labore et dolore magna aliqua. Ut enim ad minim veniam, quis nostrud.</p>
    <p>Lorem ipsum dolor sit amet, consectetur adipisicing elit, sed do eiusmod tempor incididunt ut labore et dolore magna aliqua. Ut enim ad minim veniam, quis nostrud.</p>
    <span class="btn">READ MORE</span>
  </div>
</section>

<section class="quote-band">
  <h2 class="band-title" style="left:89px;top:38px">GET A QUOTE</h2>
  <div class="field" style="left:89px;top:104px">Timeline</div>
  <div class="field select" style="left:353px;top:104px">Interior Designs</div>
  <div class="field" style="left:89px;top:172px">Name</div>
  <div class="field select" style="left:353px;top:172px">Personal</div>
  <div class="field" style="left:89px;top:240px">Phone</div>
  <div class="field" style="left:353px;top:240px">Email</div>
  <div class="field message" style="left:89px;top:309px">Message</div>
  <div class="submit">SUBMIT</div>

  <h2 class="band-title" style="left:640px;top:38px">VIDEO DEMO</h2>
  <div class="video" role="img" aria-label="Video still of a stone house under construction with arched windows">
    <div class="video-progress"><i></i></div>
    <div class="video-bar">
      <svg width="467" height="22" viewBox="0 0 467 22">
        <path d="M12 6 v10 M16 6 v10" stroke="#fff" stroke-width="2"/>
        <path d="M28 6 L36 11 L28 16 Z" fill="#fff"/>
        <rect x="46" y="8" width="4" height="6" fill="#fff"/><path d="M50 8 L56 4 V18 L50 14 Z" fill="#fff"/>
        <rect x="392" y="7" width="10" height="8" fill="none" stroke="#fff" stroke-width="1.5"/>
        <circle cx="418" cy="11" r="4" fill="none" stroke="#fff" stroke-width="1.5"/>
        <rect x="430" y="7" width="12" height="8" fill="none" stroke="#fff" stroke-width="1.5"/>
        <path d="M450 7 h4 M450 7 v4 M460 15 h-4 M460 15 v-4" stroke="#fff" stroke-width="1.5"/>
      </svg>
    </div>
  </div>
</section>

<section class="market">
  <h2 class="market-title">MARKET READY HOMES</h2>

  <article class="card" style="left:88px">
    <div class="photo" role="img" aria-label="Photo of a single-storey home with a two-car garage"></div>
    <div class="card-body">
      <h3>Work Room Design</h3>
      <div class="meta"><b>Client:</b> Northfield<br><b>Date:</b> 02/28/2016</div>
      <p>Bright open layout with a covered porch, double garage, large kitchen and quiet yard. Close to schools and parks.</p>
    </div>
    <span class="btn">READ MORE</span>
  </article>

  <article class="card" style="left:347px">
    <div class="photo" role="img" aria-label="Photo of a two-storey home with stone trim"></div>
    <div class="card-body">
      <h3>Bed Room Design</h3>
      <div class="meta"><b>Client:</b> Brightway<br><b>Date:</b> 02/28/2016</div>
      <p>Bright open layout with a covered porch, double garage, large kitchen and quiet yard. Close to schools and parks.</p>
    </div>
    <span class="btn">READ MORE</span>
  </article>

  <article class="card" style="left:607px">
    <div class="photo" role="img" aria-label="Photo of a large home with a landscaped front lawn"></div>
    <div class="card-body">
      <h3>Living Room Design</h3>
      <div class="meta"><b>Client:</b> Oakline<br><b>Date:</b> 02/28/2016</div>
      <p>Bright open layout with a covered porch, double garage, large kitchen and quiet yard. Close to schools and parks.</p>
    </div>
    <span class="btn">READ MORE</span>
  </article>

  <article class="card" style="left:866px">
    <div class="photo" role="img" aria-label="Photo of a craftsman home with gabled roof"></div>
    <div class="card-body">
      <h3>Living Room Design</h3>
      <div class="meta"><b>Client:</b> Oakline<br><b>Date:</b> 02/28/2016</div>
      <p>Bright open layout with a covered porch, double garage, large kitchen and quiet yard. Close to schools and parks.</p>
    </div>
    <span class="btn">READ MORE</span>
  </article>

  <span class="btn load-more">LOAD MORE</span>
</section>

<footer class="site-footer">
  <div class="footer-col" style="left:107px;width:230px">
    <h4><em>ABOUT</em> BUSINESS</h4>
    <p>Lorem ipsum dolor sit amet, consec-tetur adipisicing elit, sed do eiusmod tempor et incididunt ut labore et dolore</p>
  </div>
  <div class="footer-col" style="left:386px;width:220px">
    <h4><em>OUR</em> SERVICES</h4>
    <ul>
      <li>Lorem Ipsum</li>
      <li>Dolor sitmet, consectetur</li>
      <li>Adipiscing elit</li>
      <li>Vivamus porta, turpis</li>
      <li>Aliquet semperaugue</li>
      <li>Libero lobortis lacus</li>
    </ul>
  </div>
  <div class="footer-col" style="left:644px;width:240px">
    <h4><em>CONTACT</em> US</h4>
    <p>info@harborpine.com</p>
    <p style="margin-top:12px">(012) 555 0182</p>
    <p style="margin-top:12px">412 Cedar Bend Road,<br>Fairhaven, Oregon, USA</p>
    <div class="social"><span></span><span></span><span></span><span></span><span></span></div>
  </div>
  <div class="footer-col" style="left:883px;width:240px">
    <h4><em>NEWSLETTER</em> SIGN UP</h4>
    <div class="newsletter-input">
      <svg width="20" height="15" viewBox="0 0 20 15"><rect x="0.5" y="0.5" width="19" height="14" fill="#555"/><path d="M1 1 L10 8 L19 1" stroke="#fff" stroke-width="1.5" fill="none"/></svg>
      Email Adress
    </div>
    <div class="btn subscribe">SUBSCRIBE</div>
    <p style="margin-top:10px">400+ Subcribers</p>
  </div>
</footer>

<div class="copyright"><em>Harbor Pine Builders</em> © 2016 All Rights Reserved</div>

</body>
</html>
```